Bolstering Marveno Inc needs a business card design

Looking for a unique, classy and sharp business card design.

Contact Information for Business Card

Bolstering Marveno Inc.
Lidia Osorno Bermudez BScOT(c)
Occupational Therapist
(780) 555-0142
bolsteringmarveno@mailvora.com

```html
<!DOCTYPE html>
<html lang="en">
<head>
<meta charset="utf-8">
<title>Bolstering Marveno Inc. — Business Card</title>
<link href="https://fonts.googleapis.com/css2?family=Roboto:wght@400;500;700&display=swap" rel="stylesheet">
<style>
  :root {
    --stage: #e4e4e4;
    --card-white: #f7f7f7;
    --card-black: #1d1d1d;
    --purple: #8e2a93;
    --sky: #3aa7dc;
    --leaf: #8cc63f;
    --ink: #2b2b2b;
    --rule: #8a8a8a;
  }
  * { margin: 0; padding: 0; box-sizing: border-box; }
  html, body {
    width: 1200px;
    height: 923px;
    overflow: hidden;
    background: var(--stage);
    font-family: "Roboto", Arial, sans-serif;
  }
  .stage {
    width: 1200px;
    height: 923px;
    display: flex;
    flex-direction: column;
    align-items: center;
    justify-content: center;
    gap: 50px;
  }
  .card {
    width: 700px;
    height: 400px;
    position: relative;
    box-shadow: 0 6px 18px rgba(0,0,0,0.18);
  }
  .card--back {
    background: var(--card-black);
    display: flex;
    align-items: center;
    justify-content: center;
  }
  .card--front { background: var(--card-white); }

  .brand {
    display: flex;
    align-items: center;
    gap: 12px;
  }
  .brand__mark {
    width: 22px;
    height: 22px;
    border-radius: 50%;
    background: var(--leaf);
  }
  .brand__name {
    font-weight: 700;
    font-size: 30px;
    letter-spacing: -0.3px;
  }
  .card--back .brand__name { color: var(--leaf); }
  .card--front .brand {
    position: absolute;
    left: 40px;
    top: 180px;
  }
  .card--front .brand__name { color: var(--purple); font-size: 26px; }

  .divider {
    position: absolute;
    left: 430px;
    top: 40px;
    width: 1.5px;
    height: 320px;
    background: var(--rule);
  }
  .person {
    position: absolute;
    left: 458px;
    top: 66px;
  }
  .person__name {
    color: var(--purple);
    font-size: 15px;
    font-weight: 400;
  }
  .person__title {
    color: var(--sky);
    font-size: 13px;
    margin-top: 3px;
  }
  .contact {
    position: absolute;
    left: 458px;
    top: 268px;
    list-style: none;
  }
  .contact__item {
    display: flex;
    align-items: center;
    gap: 9px;
    font-size: 13px;
    color: var(--ink);
    margin-bottom: 9px;
  }
  .contact__icon {
    width: 14px;
    height: 14px;
    background: var(--leaf);
    display: flex;
    align-items: center;
    justify-content: center;
  }
</style>
</head>
<body>
<main class="stage">
  <section class="card card--back">
    <div class="brand">
      <span class="brand__mark"></span>
      <span class="brand__name">Bolstering Marveno Inc.</span>
    </div>
  </section>

  <section class="card card--front">
    <div class="brand">
      <span class="brand__mark"></span>
      <span class="brand__name">Bolstering Marveno Inc.</span>
    </div>

    <div class="divider"></div>

    <div class="person">
      <p class="person__name">Lidia Osorno Bermudez BScOT(c)</p>
      <p class="person__title">Occupational Therapist</p>
    </div>

    <ul class="contact">
      <li class="contact__item">
        <span class="contact__icon">
          <svg width="10" height="10" viewBox="0 0 24 24"><path fill="#fff" d="M6.6 10.8a15.1 15.1 0 0 0 6.6 6.6l2.2-2.2a1 1 0 0 1 1-.25 11.4 11.4 0 0 0 3.6.57 1 1 0 0 1 1 1V20a1 1 0 0 1-1 1A17 17 0 0 1 3 4a1 1 0 0 1 1-1h3.5a1 1 0 0 1 1 1c0 1.25.2 2.45.57 3.57a1 1 0 0 1-.25 1z"/></svg>
        </span>
        (780) 555-0142
      </li>
      <li class="contact__item">
        <span class="contact__icon">
          <svg width="10" height="10" viewBox="0 0 24 24"><path fill="none" stroke="#fff" stroke-width="2.5" d="M3 6h18v12H3z M3 6l9 7 9-7"/></svg>
        </span>
        bolsteringmarveno@mailvora.com
      </li>
    </ul>
  </section>
</main>
</body>
</html>
```